Business Card and Simple Logo Desgin

New Zealand based start up company "Brava Advisory LTD" requires business cards and simple logo design.

Card Content.

Brava Advisory LTD

Rosalind Kettering
CA, BMS (Hons)

r.kettering@bravaadvisory.example.nz
PH +64 21 705 146

Target Market(s)

Corporate Business in IT, Finance and accounting.

Industry/Entity Type

Business

```html
<!DOCTYPE html>
<html lang="en">
<head>
<meta charset="utf-8">
<title>Brava Advisory LTD – Business Card</title>
<link rel="stylesheet" href="https://fonts.googleapis.com/css2?family=Didact+Gothic&display=swap">
<style>
  :root {
    --backdrop: #2a2a2a;
    --card-top: #ffffff;
    --card-bottom: #e4e4e4;
    --band: #0b0b0b;
    --band-text: #f2f2f2;
    --accent: #e8731f;
    --ink: #2b2b2b;
    --rule: #7a7a7a;
    --bubble-soft: rgba(190, 190, 190, 0.0);
    --bubble-tone: rgba(190, 190, 190, 0.55);
  }
  * { box-sizing: border-box; margin: 0; padding: 0; }
  html, body {
    width: 1200px;
    height: 900px;
    overflow: hidden;
    background: var(--backdrop);
    font-family: "Didact Gothic", "Century Gothic", sans-serif;
  }
  .card {
    position: absolute;
    left: 105px;
    top: 175px;
    width: 990px;
    height: 550px;
    background: linear-gradient(160deg, var(--card-top) 0%, var(--card-top) 35%, var(--card-bottom) 100%);
    overflow: hidden;
    box-shadow: 0 12px 30px rgba(0, 0, 0, 0.5);
  }
  .card__texture {
    position: absolute;
    left: 0;
    right: 0;
    bottom: 62px;
    height: 200px;
    background: linear-gradient(to bottom, var(--bubble-soft) 0%, var(--bubble-tone) 100%);
  }
  .card__band {
    position: absolute;
    left: 0;
    right: 0;
    bottom: 0;
    height: 62px;
    background: var(--band);
    display: flex;
    align-items: center;
    justify-content: center;
  }
  .card__website {
    color: var(--band-text);
    font-size: 25px;
    letter-spacing: 0.5px;
  }
  .brand {
    position: absolute;
    left: 95px;
    top: 208px;
    display: flex;
    align-items: center;
    gap: 14px;
  }
  .brand__dot {
    width: 22px;
    height: 22px;
    border-radius: 50%;
    background: var(--accent);
  }
  .brand__name {
    font-size: 38px;
    color: var(--ink);
    letter-spacing: 0.3px;
  }
  .card__divider {
    position: absolute;
    left: 548px;
    top: 145px;
    width: 5px;
    height: 175px;
    background: var(--rule);
  }
  .contact {
    position: absolute;
    left: 590px;
    top: 150px;
  }
  .contact__name,
  .contact__credentials {
    color: var(--accent);
    font-size: 27px;
    line-height: 1.12;
  }
  .contact__details {
    margin-top: 26px;
    color: var(--ink);
    font-size: 20px;
    line-height: 1.35;
  }
</style>
</head>
<body>
  <article class="card">
    <div class="card__texture" role="img" aria-label="Soft grey bubble pattern along the lower edge of the card"></div>

    <div class="brand">
      <span class="brand__dot"></span>
      <span class="brand__name">Brava Advisory LTD</span>
    </div>

    <div class="card__divider"></div>

    <div class="contact">
      <p class="contact__name">Rosalind Kettering</p>
      <p class="contact__credentials">CA, BMS (Hons)</p>
      <div class="contact__details">
        <p class="contact__email">r.kettering@bravaadvisory.example.nz</p>
        <p class="contact__phone">PH +64 21 705 146</p>
      </div>
    </div>

    <footer class="card__band">
      <span class="card__website">www.bravaadvisory.example.nz</span>
    </footer>
  </article>
</body>
</html>
```